redesign of web page www.roverandpipswildwagon.com

id like you to redesign our web page fresh new look using our icons and pics on page and ones I will upload can use wording from web page we are a mobile zoo that comes to your location for birthdays and also public events if we could have few pages one that is for birthdays one for events and one for animal removal we are fully licensed for native and pest animal relocation we use Linux hosting Dreamweaver upload
we do school fetes kindergartens aged care disability and more our web page now
www.roverandpipswildwagon.com

Target Market(s)

public events schools kindergartens aged care

Number of Pages Required

1 page

Font styles to use
Script

Requirements
Must have
• that we have full range of native animals to interact with and learn about or grate wildlife face book link https://www.facebook.com/RoverAndPipsWildWagon/
• can use photos of page
• and donation link as well

```html
<!DOCTYPE html>
<html lang="en">
<head>
<meta charset="utf-8">
<title>Rover &amp; Pip's Wild Wagon</title>
<link href="https://fonts.googleapis.com/css2?family=Lato:wght@400;700&display=swap" rel="stylesheet">
<style>
:root{
  --brown:#8e5a2c;
  --brown-dark:#7d4c22;
  --green:#5f9a3e;
  --orange:#f7a326;
  --ink:#2c4656;
  --text:#555;
  --rule:#e2e2e2;
}
*{margin:0;padding:0;box-sizing:border-box}
html,body{width:827px;height:1200px;overflow:hidden;background:#fff;font-family:'Lato',sans-serif;color:var(--text)}
.page{position:relative;width:827px;height:1200px}
.abs{position:absolute}
.brand{left:69px;top:14px;display:flex;align-items:center;gap:6px;font-weight:700;font-size:15px;color:var(--green);line-height:1.1;width:120px}
.brand .dot{width:12px;height:12px;border-radius:50%;background:var(--brown);flex:none}
.contact-item{top:32px;font-size:10px;color:#333;display:flex;align-items:center;gap:6px}
.divider{left:433px;top:30px;width:1px;height:18px;background:#ccc}
.donate{left:669px;top:24px;width:91px;height:29px;background:linear-gradient(#fbb946,var(--orange));color:#fff;font-size:11px;display:flex;align-items:center;justify-content:center;letter-spacing:.3px}
.cards{left:696px;top:57px;display:flex;gap:4px}
.cards span{width:11px;height:7px;background:#cfd6e0;border:1px solid #aab}
.nav{left:68px;top:78px;width:691px;height:29px;background:var(--brown);display:flex}
.nav a{font-size:9px;color:#fff;text-decoration:none;display:flex;align-items:center;justify-content:center;border-right:1px solid #a06c3d}
.nav a.active{background:var(--green)}
.hero{left:68px;top:115px;width:691px;height:338px;box-shadow:0 8px 12px -6px rgba(0,0,0,.35);
  background:
    radial-gradient(ellipse 90px 110px at 78% 48%,#e7b9a0 0%,#d9a48a 55%,rgba(217,164,138,0) 100%),
    radial-gradient(ellipse 170px 110px at 76% 90%,#b9c0d6 0%,#8e98b8 50%,rgba(142,152,184,0) 100%),
    radial-gradient(ellipse 160px 120px at 38% 45%,#4c4339 0%,rgba(76,67,57,0) 100%),
    linear-gradient(120deg,#6d665c 0%,#7d7568 45%,#8a7c6a 70%,#b48455 100%)}
.arrow{top:264px;width:25px;height:25px;border-radius:50%;background:rgba(200,200,200,.6);display:flex;align-items:center;justify-content:center}
.caption{left:100px;top:343px;width:373px;height:92px;background:rgba(30,30,30,.75);padding:12px 16px;color:#fff;font-size:11px;line-height:1.7}
.caption .btns{display:flex;gap:3px;margin-top:8px}
.btn{font-size:9px;color:#fff;padding:4px 9px}
.btn.green{background:var(--green)}.btn.brown{background:var(--brown)}
.h2{font-size:15px;color:var(--ink);font-weight:700;display:flex;align-items:center;gap:8px}
.h2::before{content:"";width:5px;height:5px;background:var(--green);box-shadow:-1px -1px 0 var(--brown)}
.intro{left:85px;top:520px;width:658px;text-align:center;font-size:8px;line-height:1.5}
.more{font-size:8px;display:flex;align-items:center;gap:4px}
.thumb{width:146px;height:110px;border:1px solid #ddd}
.thumb-cap{width:146px;text-align:center;font-size:10.5px;color:#222;line-height:1.35}
.tabs{left:569px;top:634px;width:160px;height:28px;display:flex;font-size:8px;color:#fff}
.tabs div{display:flex;align-items:center;justify-content:center}
.tabs .on{width:81px;background:var(--green);border-top:2px solid var(--brown)}
.tabs .off{flex:1;background:var(--brown)}
.quote{left:569px;width:160px;border-bottom:1px solid var(--rule);padding:0 3px 8px;font-size:8px;color:#222;line-height:1.8}
.quote small{display:block;color:#999;font-size:6.5px;margin-bottom:2px}
.footer{left:68px;top:989px;width:692px;height:211px;background:var(--brown)}
.footer .bar{position:absolute;left:0;bottom:0;width:100%;height:40px;background:var(--brown-dark);font-size:7px;color:#fff;display:flex;align-items:center;justify-content:space-between;padding:0 24px 0 19px}
.fcol{top:33px;color:#fff}
.fcol h4{font-size:8.5px;font-weight:400;margin-bottom:10px}
.fcol p{font-size:7px;line-height:1.45;color:#f4e6d8}
.fcol ul{list-style:none;font-size:7px;color:#f4e6d8}
.fcol li{margin-bottom:5.5px;display:flex;gap:10px;align-items:center}
.fcol li::before{content:"";width:3px;height:3px;border-radius:50%;background:#fff}
.field{width:137px;height:19px;background:#a56e3e;border:1px solid #b98555;color:#fff;font-size:7px;padding:5px 6px;margin-top:6px;display:flex;justify-content:space-between}
.social{display:flex;gap:6px;align-items:center}
.social span{width:7px;height:7px;border:1px solid #fff;border-radius:2px}
</style>
</head>
<body>
<div class="page">
  <div class="abs brand"><span class="dot"></span>Rover &amp; Pip's Wild Wagon</div>
  <div class="abs contact-item" style="left:301px">
    <svg width="10" height="12" viewBox="0 0 10 12"><path d="M2 1 L4 1 L5 4 L3.5 5 Q5 8 6.5 9 L7.5 7.5 L10 8.5 L10 11 Q4 12 1 4 Z" fill="#9a5a2a"/></svg>
    phone: 0400 000 123</div>
  <div class="abs divider"></div>
  <div class="abs contact-item" style="left:454px">
    <svg width="11" height="10" viewBox="0 0 11 10"><rect x="0.5" y="1.5" width="10" height="8" fill="none" stroke="#5f9a3e"/><path d="M0.5 1.5 L5.5 6 L10.5 1.5" fill="none" stroke="#5f9a3e"/></svg>
    hello@wildwagonmail.com</div>
  <div class="abs donate">DONATE</div>
  <div class="abs cards"><span></span><span></span><span></span></div>

  <nav class="abs nav">
    <a class="active" style="width:78px">HOME</a>
    <a style="width:95px">ABOUT US</a>
    <a style="width:104px">ABOUT US</a>
    <a style="width:116px">THE ANIMALS</a>
    <a style="width:102px">THE SHOW</a>
    <a style="width:83px">LINKS</a>
    <a style="flex:1;border:none">CONTACT US</a>
  </nav>

  <div class="abs hero" role="img" aria-label="Photo of a baby lying in a cosy corduroy beanbag beside a small native animal"></div>
  <div class="abs arrow" style="left:85px"><svg width="8" height="12"><path d="M6 1 L1 6 L6 11" fill="none" stroke="#555" stroke-width="1.5"/></svg></div>
  <div class="abs arrow" style="left:717px"><svg width="8" height="12"><path d="M2 1 L7 6 L2 11" fill="none" stroke="#eee" stroke-width="1.5"/></svg></div>
  <div class="abs caption">A huge range of native animals with fully qualified skilled handlers to help you get the most from this experience.
    <div class="btns"><span class="btn green">Read More</span><span class="btn brown">Contact Now</span></div>
  </div>

  <h2 class="abs h2" style="left:325px;top:481px">Welcome To Our SIte</h2>
  <p class="abs intro">A huge range of native animals with fully qualified skilled handlers to help you get the most from this experience. Great for birthday parties, kindergartens, schools and all public events. Based in Fernvale, Victoria but traveling to a wide range of surrounding areas.</p>
  <div class="abs more" style="left:400px;top:573px">More <svg width="9" height="9"><circle cx="4.5" cy="4.5" r="3.8" fill="none" stroke="#555"/><path d="M2.5 4.5 H6.5 M5 3 L6.5 4.5 L5 6" fill="none" stroke="#555"/></svg></div>

  <h2 class="abs h2" style="left:65px;top:600px">Gallery</h2>
  <svg class="abs" style="left:521px;top:604px" width="14" height="10"><path d="M5 1 L1 5 L5 9 M9 1 L13 5 L9 9" fill="none" stroke="#3a6fa8" stroke-width="1.3"/></svg>

  <div class="abs thumb" style="left:68px;top:632px;background:radial-gradient(ellipse 45px 45px at 58% 52%,#7d7770 0%,#a19b94 55%,rgba(255,255,255,0) 100%),linear-gradient(#fbfbfb,#f1f0ee 80%,#8fb070 92%,#f4f4f2)" role="img" aria-label="Photo of a common wombat"></div>
  <div class="abs thumb" style="left:230px;top:632px;background:radial-gradient(ellipse 55px 45px at 40% 55%,#5a4f44 0%,#6d6254 60%,rgba(109,98,84,0) 100%),linear-gradient(90deg,#8a8068 0%,#7a7262 60%,#4f6a3a 85%,#6e8a54 100%)" role="img" aria-label="Photo of a southern hairy nosed wombat"></div>
  <div class="abs thumb" style="left:391px;top:632px;background:radial-gradient(ellipse 55px 30px at 50% 55%,#c7792e 0%,#d9914a 55%,rgba(217,145,74,0) 100%),linear-gradient(#7e96b0 0%,#a9b8c4 25%,#d9c7a9 40%,#e3d2b5 100%)" role="img" aria-label="Photo of a dingo on a beach"></div>
  <div class="abs thumb-cap" style="left:68px;top:752px">The Common Wombat</div>
  <div class="abs thumb-cap" style="left:230px;top:752px">The Southern Hairy Nosed Wombat</div>
  <div class="abs thumb-cap" style="left:391px;top:752px">The Dingo</div>

  <div class="abs thumb" style="left:68px;top:804px;background:radial-gradient(ellipse 55px 30px at 45% 55%,#5c4a3a 0%,#6e5a46 55%,rgba(110,90,70,0) 100%),linear-gradient(135deg,#a07a55,#7d6048 50%,#b08a62)" role="img" aria-label="Photo of a brushtail bettong"></div>
  <div class="abs thumb" style="left:230px;top:804px;background:radial-gradient(ellipse 55px 25px at 50% 60%,#8fc84a 0%,#a8d66a 50%,rgba(255,255,255,0) 100%),#fdfdfb" role="img" aria-label="Photo of a green tree python"></div>
  <div class="abs thumb" style="left:391px;top:804px;background:radial-gradient(ellipse 35px 45px at 55% 55%,#5e5646 0%,#877d6a 50%,rgba(255,255,255,0) 100%),linear-gradient(#fff 20%,#e9d9bf 22%,#fff 25%)" role="img" aria-label="Photo of an olive python on a branch"></div>
  <div class="abs thumb-cap" style="left:68px;top:923px">The Brushtail Bettong</div>
  <div class="abs thumb-cap" style="left:230px;top:923px">The Green Tree Python</div>
  <div class="abs thumb-cap" style="left:391px;top:923px">The Olive Python</div>

  <h2 class="abs h2" style="left:568px;top:600px">Links &amp; Testimonials</h2>
  <div class="abs tabs"><div class="on">Testimonials</div><div class="off">Links</div></div>
  <div class="abs quote" style="top:677px"><small>July 27, 2015</small>We had Rover and Pip for Tobys 7th Birthday on the weekend. Thanks and what a great job, 9 boys and 6</div>
  <div class="abs quote" style="top:748px"><small>July 27, 2015</small>Awesome job this morning for Brackenridge family daycare people, loved it, thank you :Dnatoque</div>
  <div class="abs quote" style="top:819px"><small>July 27, 2015</small>I will definitely be looking at booking you guys for my Mia's next birthday :) (Pip)sociis natoque</div>
  <div class="abs quote" style="top:890px"><small>July 27, 2015</small>Aliquam auctor rutrum metus, id vulpu-tate ante. Praesent ligula justo, luctus in consequat quis, tempus a neque. Cum</div>

  <footer class="abs footer">
    <div class="abs fcol" style="left:19px;width:160px">
      <h4>WHO WE ARE</h4>
      <p>Lorem ipsum dolor sit amet, consectetur adipiscing elit. Nullam venenatis velit blandit est condimentum aliquet. Curabitur ut libero justo. Nulla ut ex facilisis, tincidunt quam vitae, iaculis orci. Nullam eu faucibus nibh.</p>
      <div class="more" style="color:#fff;margin:12px 0 0 112px">More <svg width="9" height="9"><circle cx="4.5" cy="4.5" r="3.8" fill="none" stroke="#fff"/><path d="M2.5 4.5 H6.5 M5 3 L6.5 4.5 L5 6" fill="none" stroke="#fff"/></svg></div>
    </div>
    <div class="abs fcol" style="left:238px"><h4>USEFUL LINKS 1</h4>
      <ul><li>Home</li><li>About Us</li><li>The Animals</li><li>The Show</li><li>Limks</li></ul></div>
    <div class="abs fcol" style="left:380px"><h4>USEFUL LINKS 2</h4>
      <ul><li>About US</li><li>THe Show</li><li>Gallery</li><li>Contact Us</li></ul></div>
    <div class="abs fcol" style="left:534px;width:145px"><h4>CONTACT</h4>
      <p>Doloreiur quia commolu ptatemp dolupta oreprerum</p>
      <div class="field" style="margin-top:9px">Email</div>
      <div class="field">Contact For <span>&#8964;</span></div>
      <div class="btn green" style="display:inline-block;margin:8px 0 0 84px;font-size:7.5px;padding:3px 9px">CONTACT</div>
    </div>
    <div class="bar"><span>© 2015 yoursite. All rights reserved.</span>
      <div class="social" aria-label="Social links"><span></span><span></span><span></span><span></span></div></div>
  </footer>
</div>
</body>
</html>
```